Glow Up by Lakeside 21 day Challenge

We are having a Glow Up by Lakeside Challenge at our fitness studio. We need a poster design using the template attached as a reference. I have also included our Bromalux logo to put on the poster. Please DO NOT use the graphics in the flyer as we are expecting something much better :-)

-Size needed 11x17 with bleeding for printing

-We need this made in Photoshop (CS3 friendly) or at least delivered in PS as we might change some text or re-arrange the design later on.

-We need this in layers.

```html
<!DOCTYPE html>
<html lang="en">
<head>
<meta charset="utf-8">
<title>Glow Up by Lakeside Challenge Poster</title>
<link href="https://fonts.googleapis.com/css2?family=Montserrat:wght@900&family=PT+Sans+Narrow:wght@700&display=swap" rel="stylesheet">
<style>
  :root {
    --page: #8e8f90;
    --mint: #dff5cf;
    --aqua: #9fe0cf;
    --teal: #5fcfc6;
    --blue: #0aa4e8;
    --red: #e8202f;
    --yellow: #fff200;
    --black: #0b0b0b;
    --white: #ffffff;
    --ink: #222222;
  }
  * { margin: 0; padding: 0; box-sizing: border-box; }
  html, body { width: 1182px; height: 1200px; overflow: hidden; background: var(--page); }
  .poster {
    position: absolute; left: 216px; top: 20px; width: 750px; height: 1160px;
    overflow: hidden; font-family: "PT Sans Narrow", "Arial Narrow", sans-serif; font-weight: 700;
  }
  .poster-shapes { position: absolute; inset: 0; }
  .headline {
    position: absolute; right: 105px; top: 62px; text-align: right;
    font-family: "Montserrat", sans-serif; font-weight: 900; color: var(--blue);
    font-size: 76px; line-height: 68px; letter-spacing: -4px; text-transform: uppercase;
  }
  .tagline { position: absolute; font-size: 34px; line-height: 34px; color: var(--white);
    text-transform: uppercase; text-align: center; font-weight: 700; }
  .tagline-black { background: var(--black); }
  .tagline-red { background: var(--red); }
  .tag-1 { left: 278px; top: 309px; width: 419px; }
  .tag-2 { left: 207px; top: 345px; width: 481px; }
  .tag-3 { left: 321px; top: 381px; width: 325px; }
  .benefit { position: absolute; font-size: 13px; line-height: 16px; text-align: center; color: var(--ink); }
  .benefit-blue { color: var(--white); }
  .b1 { left: 310px; top: 468px; width: 94px; }
  .b2 { left: 441px; top: 505px; width: 76px; }
  .b3 { left: 583px; top: 487px; width: 74px; }
  .b4 { left: 537px; top: 598px; width: 84px; }
  .badge-num { position: absolute; width: 30px; text-align: center; font-family: "Montserrat", sans-serif;
    font-weight: 900; font-size: 17px; line-height: 30px; color: var(--ink); }
  .offer { position: absolute; left: 188px; top: 694px; width: 180px; text-align: center;
    color: var(--ink); font-size: 28px; line-height: 26px; }
  .offer-price { display: block; margin-top: 4px; font-family: "Montserrat", sans-serif; font-weight: 900;
    font-size: 56px; line-height: 58px; color: var(--red); letter-spacing: -2px; }
  .quote-mark { position: absolute; font-family: "Montserrat", sans-serif; font-weight: 900;
    font-size: 110px; line-height: 110px; color: var(--blue); }
  .quote-open { left: 447px; top: 762px; }
  .quote-close { left: 600px; top: 860px; }
  .quote-text { position: absolute; left: 494px; top: 833px; width: 94px; font-size: 15px; line-height: 17px; color: var(--ink); }
  .quote-author { display: block; font-size: 10px; line-height: 13px; white-space: nowrap; }
  .brand { position: absolute; left: 186px; top: 953px; width: 258px; height: 78px;
    display: flex; align-items: center; justify-content: center; gap: 10px; white-space: nowrap;
    font-size: 28px; color: var(--white); text-transform: uppercase; }
  .brand-mark { width: 14px; height: 14px; background: var(--blue); flex: none; }
  .hurry { position: absolute; left: 52px; top: 1066px; font-family: "Montserrat", sans-serif; font-weight: 900;
    font-size: 28px; color: var(--red); transform: rotate(-8deg); }
  .limited { position: absolute; left: 190px; top: 1054px; width: 240px; text-align: center;
    color: var(--white); font-size: 19px; line-height: 16px; text-transform: uppercase; }
  .contact { position: absolute; left: 150px; top: 1116px; width: 300px; text-align: center;
    color: var(--red); font-size: 22px; text-transform: uppercase; }
</style>
</head>
<body>
<main class="poster">
  <svg class="poster-shapes" width="750" height="1160" viewBox="0 0 750 1160">
    <defs>
      <linearGradient id="wash" x1="0" y1="0" x2="0" y2="1">
        <stop offset="0" stop-color="var(--mint)"/>
        <stop offset="0.45" stop-color="var(--aqua)"/>
        <stop offset="0.8" stop-color="var(--teal)"/>
      </linearGradient>
      <linearGradient id="beachLeft" x1="0" y1="0" x2="0" y2="1">
        <stop offset="0" stop-color="#3fa6c4"/>
        <stop offset="0.5" stop-color="#d9b08f"/>
        <stop offset="1" stop-color="#ece6dc"/>
      </linearGradient>
      <linearGradient id="beachRight" x1="0" y1="0" x2="0" y2="1">
        <stop offset="0" stop-color="#4aa9c6"/>
        <stop offset="0.45" stop-color="#c99a7a"/>
        <stop offset="1" stop-color="#f1ede6"/>
      </linearGradient>
    </defs>
    <rect class="background-wash" width="750" height="1160" fill="url(#wash)"/>
    <path class="footer-band" d="M0,900 Q375,830 750,870 L750,1160 L0,1160 Z" fill="var(--black)"/>
    <circle cx="107" cy="577" r="368" fill="var(--black)"/>
    <circle class="photo-left" cx="107" cy="577" r="356" fill="url(#beachLeft)" role="img" aria-label="Photo of a smiling woman in a white bikini walking along the beach"/>
    <circle cx="730" cy="911" r="238" fill="var(--black)"/>
    <circle class="photo-right" cx="730" cy="911" r="228" fill="url(#beachRight)" role="img" aria-label="Photo of a fit man in white trousers standing at the shoreline"/>

    <circle cx="358" cy="513" r="76" fill="var(--yellow)"/>
    <circle cx="478" cy="547" r="60" fill="var(--blue)"/>
    <circle cx="620" cy="527" r="65" fill="var(--yellow)"/>
    <circle cx="578" cy="643" r="67" fill="var(--blue)"/>

    <circle cx="307" cy="445" r="15" fill="var(--yellow)" stroke="var(--blue)" stroke-width="3"/>
    <circle cx="527" cy="508" r="15" fill="var(--white)" stroke="var(--yellow)" stroke-width="3"/>
    <circle cx="674" cy="499" r="15" fill="var(--yellow)" stroke="var(--blue)" stroke-width="3"/>
    <circle cx="638" cy="617" r="15" fill="var(--white)" stroke="var(--yellow)" stroke-width="3"/>

    <circle cx="410" cy="460" r="8" fill="var(--blue)"/><circle cx="419" cy="454" r="4" fill="var(--red)"/>
    <circle cx="412" cy="593" r="8" fill="var(--yellow)"/><circle cx="421" cy="588" r="4" fill="var(--red)"/>
    <circle cx="574" cy="477" r="8" fill="var(--red)"/><circle cx="583" cy="471" r="4" fill="var(--blue)"/>
    <circle cx="680" cy="552" r="4" fill="var(--blue)"/>
    <circle cx="510" cy="658" r="11" fill="var(--yellow)"/><circle cx="522" cy="650" r="5" fill="var(--red)"/>

    <circle cx="278" cy="781" r="128" fill="var(--white)"/>
    <path d="M150,781 A128,128 0 0 0 400,830" fill="none" stroke="var(--blue)" stroke-width="5"/>
    <circle cx="538" cy="870" r="84" fill="var(--white)"/>
    <path d="M460,900 A84,84 0 0 0 610,915" fill="none" stroke="var(--blue)" stroke-width="5"/>

    <line x1="43" y1="1111" x2="450" y2="1111" stroke="var(--blue)" stroke-width="1.5"/>
  </svg>

  <h1 class="headline">Glow Up<br>by<br>Lakeside</h1>

  <p class="tagline tagline-black tag-1">Discover the secret</p>
  <p class="tagline tagline-red tag-2">to a beach-ready body</p>
  <p class="tagline tagline-black tag-3">in just 21 days!</p>

  <span class="badge-num" style="left:292px;top:430px">1</span>
  <span class="badge-num" style="left:512px;top:493px">2</span>
  <span class="badge-num" style="left:659px;top:484px">3</span>
  <span class="badge-num" style="left:623px;top:602px">4</span>

  <p class="benefit b1">9 total training sessions designed to incinerate fat off your midsection, thighs and arms</p>
  <p class="benefit benefit-blue b2">21 days of nutritional guidance, including delicious recipes</p>
  <p class="benefit b3">A Success Session to map out your individual plan for success</p>
  <p class="benefit benefit-blue b4">Your very own Personal Accountability Coach to ensure you get results</p>

  <p class="offer">You get all this - a $399 value - for ONLY<span class="offer-price">$99!</span></p>

  <span class="quote-mark quote-open">“</span>
  <p class="quote-text">I've never been more fit in my life- at age 41!<span class="quote-author">-Marisol Deane</span></p>
  <span class="quote-mark quote-close">”</span>

  <div class="brand"><span class="brand-mark"></span>Bromalux Bootcamps</div>

  <p class="hurry">HURRY!</p>
  <p class="limited">Space is limited to only<br>20 participants!!!<br>Claim your spot now:</p>
  <p class="contact">Website and phone number</p>
</main>
</body>
</html>
```